Business card design for new brand

We have recently rebranded and need a new business card template.

We are an insurance underwriting agency. All of our products are sold via other partner companies, so these are just to pass on our details to other organisations.

We would like to see designs that use the colour green (current stationary generally uses lime green (rgb 142,190,63) and forest green (0,154,79) to comply with our logo's colours. We are happy with other shades of green.

Business cards need to include our logo, as well as space for:
1. Full name
2. Qualifications (optional)
3. Title
4. Office number
5. Mobile number
6. Email address

Our logo is enclosed here.

```html
<!DOCTYPE html>
<html lang="en">
<head>
<meta charset="utf-8">
<title>Fernvale Underwriters – Business Card</title>
<link rel="stylesheet" href="https://fonts.googleapis.com/css2?family=Arimo:wght@400;700&display=swap">
<style>
  :root {
    --stage: #0b0b0b;
    --card: #262626;
    --card-edge: #009a4f;
    --forest: #009a4f;
    --lime: #8ebe3f;
    --rule: #a8b820;
    --white: #ffffff;
    --grey: #d4d4d4;
    --faint: #3a3a3a;
  }
  * { box-sizing: border-box; margin: 0; padding: 0; }
  html, body { width: 1200px; height: 820px; overflow: hidden; }
  body {
    background: radial-gradient(ellipse at 50% 40%, #1c1c1c 0%, var(--stage) 75%);
    font-family: "Arimo", Arial, sans-serif;
    position: relative;
  }
  .card {
    position: absolute;
    top: 255px;
    width: 540px;
    height: 310px;
    background: var(--card);
    border: 2px solid var(--card-edge);
    box-shadow: 0 18px 40px rgba(0,0,0,.7);
  }
  .card--front { left: 40px; }
  .card--back { left: 620px; }

  /* front */
  .brand {
    position: absolute;
    left: 150px;
    top: 52px;
    display: flex;
    align-items: center;
    gap: 14px;
  }
  .brand__square { width: 30px; height: 30px; background: var(--forest); }
  .brand__name {
    color: var(--white);
    font-weight: 400;
    font-size: 25px;
    line-height: 1.15;
    letter-spacing: .5px;
  }
  .rule {
    position: absolute;
    height: 1px;
    background: var(--rule);
  }
  .rule--top { left: 180px; right: 28px; top: 138px; }
  .rule--bottom { left: 28px; width: 180px; top: 224px; }
  .person {
    position: absolute;
    left: 28px;
    top: 170px;
  }
  .person__name { color: var(--forest); font-weight: 700; font-size: 22px; }
  .person__title { color: var(--grey); font-size: 13px; margin-top: 3px; }
  .contacts {
    position: absolute;
    left: 28px;
    top: 234px;
    list-style: none;
  }
  .contacts li {
    display: flex;
    align-items: center;
    gap: 9px;
    color: var(--grey);
    font-size: 13px;
    line-height: 20px;
  }
  .contacts svg { width: 14px; height: 14px; flex: none; }

  /* back */
  .back-mark {
    position: absolute;
    left: 70px;
    top: 120px;
    width: 140px;
    height: 140px;
    background: linear-gradient(135deg, #4a4a4a, var(--faint));
    transform: rotate(45deg);
  }
  .back-brand {
    position: absolute;
    right: 30px;
    top: 40px;
    color: var(--white);
    font-weight: 400;
    font-size: 25px;
    text-align: right;
    line-height: 1.15;
  }
</style>
</head>
<body>
  <section class="card card--front" aria-label="Business card front">
    <div class="brand">
      <span class="brand__square"></span>
      <span class="brand__name">Fernvale<br>Underwriters Pty Ltd</span>
    </div>
    <div class="rule rule--top"></div>
    <div class="person">
      <p class="person__name">Marcus Hale</p>
      <p class="person__title">Managing Director</p>
    </div>
    <div class="rule rule--bottom"></div>
    <ul class="contacts">
      <li>
        <svg viewBox="0 0 16 16" aria-hidden="true"><path d="M4 1.5l2.5 3-1.5 1.5a8 8 0 0 0 5 5l1.5-1.5 3 2.5-1.5 2.5C7 14 2 9 1.5 3z" fill="none" stroke="#009a4f" stroke-width="1.6" stroke-linejoin="round"/></svg>
        041-555 210 384
      </li>
      <li>
        <svg viewBox="0 0 16 16" aria-hidden="true"><rect x="4" y="1" width="8" height="14" rx="1.5" fill="none" stroke="#009a4f" stroke-width="1.6"/><line x1="7" y1="12.5" x2="9" y2="12.5" stroke="#009a4f" stroke-width="1.4"/></svg>
        041-555 210 385
      </li>
      <li>
        <svg viewBox="0 0 16 16" aria-hidden="true"><rect x="1" y="3" width="14" height="10" fill="#009a4f"/><path d="M1 3l7 6 7-6" fill="none" stroke="#262626" stroke-width="1.3"/></svg>
        info@fernvale.com
      </li>
    </ul>
  </section>

  <section class="card card--back" aria-label="Business card back">
    <div class="back-mark"></div>
    <p class="back-brand">Fernvale<br>Underwriters Pty Ltd</p>
  </section>
</body>
</html>
```